FLC 4172 KORVELL AIRPORT Crumbs and Comets

Design a poster to promote an event at our airport. We host a pancake and sausage breakfast every year to promote aviation at our airport. About 2000 people attend. The theme here at the airport definitely steers toward classic 1950s looks. We decorate with a lot of WWII aircraft and pin up girls. NO TOO RISKE' Tho, as it is a family event. I was thinking something with a R9 Halvard. I would need a blank spot at the bottom for pasting in sponsorship logos. I've attached the last 3 years flyers for reference. The date is June 8, 2025 from 8:30 am to noon.

Target Market(s)

All (family friendly)

Industry/Entity Type

Aviation

Requirements
Must have
• A 1950s theme with an airplane
Nice to have
• R9 Halvard or K27 Brindle, Pin up girl
Should not have
• A pin up girl that shows too much skin.

```html
<!DOCTYPE html>
<html lang="en">
<head>
<meta charset="utf-8">
<title>Korvell Fly-In</title>
<link rel="stylesheet" href="https://fonts.googleapis.com/css2?family=Jost:wght@700&family=Oswald:wght@500;600&family=Roboto+Condensed:wght@700&family=Source+Sans+3:wght@400&display=swap">
<style>
  :root {
    --ink: #1c1c1c;
    --slate: #3d3d3d;
    --red: #e10a17;
    --orange: #ee7c4f;
    --bar: #555555;
    --paper-light: #ffffff;
    --paper-dark: #c4c4c4;
    --plane-teal: #21444d;
    --plane-tan: #efb574;
    --cloud: #a2a59f;
  }
  * { margin: 0; padding: 0; box-sizing: border-box; }
  html, body { width: 860px; height: 1200px; overflow: hidden; }
  body { background: var(--paper-dark); }
  .poster {
    position: relative;
    width: 860px;
    height: 1200px;
    overflow: hidden;
    background: radial-gradient(ellipse 70% 55% at 50% 52%, var(--paper-light) 0%, #ececec 45%, var(--paper-dark) 100%);
  }
  .event-title {
    position: absolute;
    top: 44px;
    left: 0;
    width: 860px;
    text-align: center;
    font-family: "Jost", "Futura", sans-serif;
    font-weight: 700;
    font-size: 82px;
    letter-spacing: 3px;
    color: var(--ink);
    white-space: nowrap;
  }
  .event-title .accent { color: var(--red); }
  .hero-art {
    position: absolute;
    left: 54px;
    top: 288px;
    width: 736px;
    height: 360px;
  }
  .when {
    position: absolute;
    left: 62px;
    top: 692px;
    font-family: "Oswald", "Roboto Condensed", sans-serif;
    font-weight: 600;
    font-size: 43px;
    line-height: 40px;
    color: var(--slate);
  }
  .when .hot { color: var(--red); font-family: "Roboto Condensed", sans-serif; font-weight: 700; }
  .rule {
    position: absolute;
    left: 64px;
    height: 11px;
    background: var(--bar);
  }
  .rule--short { top: 790px; width: 290px; }
  .rule--long { top: 1046px; width: 518px; }
  .tagline {
    position: absolute;
    left: 68px;
    top: 818px;
    font-family: "Roboto Condensed", sans-serif;
    font-weight: 700;
    font-size: 39px;
    color: var(--slate);
  }
  .host {
    position: absolute;
    left: 66px;
    top: 873px;
    font-family: "Source Sans 3", "Myriad Pro", sans-serif;
    font-weight: 400;
    font-size: 56px;
    color: var(--orange);
  }
  .venue {
    position: absolute;
    left: 67px;
    top: 975px;
    font-family: "Roboto Condensed", sans-serif;
    font-weight: 700;
    font-size: 36px;
    color: var(--red);
  }
</style>
</head>
<body>
  <main class="poster">
    <h1 class="event-title">KORVELL FLY - <span class="accent">IN</span></h1>

    <svg class="hero-art" role="img" aria-label="Vintage biplane illustration in teal and tan flying among grey clouds" viewBox="0 0 736 360">
      <defs>
        <linearGradient id="heroFill" x1="0" y1="0" x2="1" y2="1">
          <stop offset="0" stop-color="var(--cloud)" stop-opacity="0.55"/>
          <stop offset="0.5" stop-color="var(--plane-tan)" stop-opacity="0.75"/>
          <stop offset="1" stop-color="var(--plane-teal)" stop-opacity="0.6"/>
        </linearGradient>
      </defs>
      <rect width="736" height="360" rx="24" fill="url(#heroFill)"/>
    </svg>

    <p class="when">SUNDAY <span class="hot">8:30am</span><br>08, JUNE- <span class="hot">2025</span></p>
    <div class="rule rule--short"></div>

    <p class="tagline">Crumbs &amp; Comets</p>
    <p class="host">Flc Chapter 4172</p>
    <p class="venue">Korvell Airport</p>
    <div class="rule rule--long"></div>
  </main>
</body>
</html>
```